Media Browser and player web application

I need to redesign a web application that enables to browse a media server (Lumarra) contents (images, audio, video) and play it in a web player.

Current implementation of the application can be seen at: http://www.kelbofaq.net/content/demonstration-lumarra-pro-online-media-browser

This refresh is aiming to:
1) make the application simpler, based on typology (think Panelix Tile style, VidHalo, Flickro); a simple fan concept is here: http://tow.gandeliq.net/lumarra/
2) make the application work on desktop as well as touch screen devices (ie no hover functionality, no pagination, large touch controls)
3) fast (remove unnecessary animations)
4) design with the app being responsive in mind

The attached UX designs show the basic flows in the application. Please note that the placement of controls (for example) is not set in stone and I welcome your input on the layout.

Ideally the default theme will be dark. Items' thumbnails will be square place holders, with images fit in them depending on the item icons' aspect ratio.

Also attaching the product's logo (Lumarra) and icon. The web application's name is ClipRoamer (or Lumarra ClipRoamer), so it should be included in the design (the UX designs include place holder Lumarra logo in the left top corner).

The main categories for each file type are (you will have to provide an icon for each of these):
- Audio: Albums, Artists, Album artists, Folders, Genres, Composers, Titles, Random music, Random albums, Last listened, Playlists, Online
- Image: Albums, Folders, Year, Month, Playlists, Online
- Video: Titles, Movies, Series, Folders, Last viewed, Last added, Genres, Actors, Directors, Producers, Release years, Playlists, Online
Updates

Target Market(s)

Mostly tech enthusiasts who want to stream their media over the internet to their devices.

Industry/Entity Type

Artists

Requirements
Must have
• Designs for all the provided UX designs
Touch-friendly web application design
High-res (Retina) assets
Light, type based Tile-like design
Nice to have
• Responsive web version
Dark and Light theme switching.
Should not have
• Chrome
Heavy graphics (eg backgrounds) that take time to load

```html
<!DOCTYPE html>
<html lang="en">
<head>
<meta charset="utf-8">
<title>ClipRoamer</title>
<link rel="stylesheet" href="https://fonts.googleapis.com/css2?family=Lato:wght@400;700&display=swap">
<style>
  :root {
    --bar-bg: #1b1b1b;
    --page-bg: #313131;
    --edge: #3c3c3c;
    --accent: #e6c01c;
    --text-light: #ffffff;
    --text-muted: #8a8a8a;
    --mark-muted: #5a5a5a;
    --tile-start: #6688b6;
    --tile-end: #92adcd;
    --tile-edge: #a1b7d4;
  }
  * { box-sizing: border-box; margin: 0; padding: 0; }
  html, body {
    width: 1200px; height: 715px; overflow: hidden;
    background: var(--page-bg);
    font-family: "Lato", sans-serif;
  }
  .app { position: relative; width: 1200px; height: 715px; }

  .top-bar {
    position: absolute; left: 0; top: 0; width: 1200px; height: 32px;
    background: var(--bar-bg);
    border-bottom: 1px solid var(--edge);
  }
  .user-menu {
    position: absolute; left: 958px; top: 9px;
    display: flex; align-items: center; gap: 6px;
    color: var(--accent); font-size: 11px;
  }
  .user-menu svg { display: block; }

  .workspace {
    position: absolute; left: 0; top: 32px; width: 1200px; height: 640px;
    border-left: 1px solid var(--edge); border-right: 1px solid var(--edge);
  }
  .brand {
    position: absolute; left: 94px; top: 24px;
    display: flex; align-items: center; gap: 9px;
  }
  .brand-square {
    width: 31px; height: 31px; border-radius: 5px; background: var(--accent);
  }
  .brand-name {
    color: var(--text-light); font-weight: 700; font-size: 22px; letter-spacing: 1.2px;
  }

  .categories {
    position: absolute; left: 348px; top: 220px;
    display: flex; gap: 10px;
  }
  .category-tile {
    position: relative; width: 162px; height: 162px;
    background: linear-gradient(135deg, var(--tile-start) 0%, var(--tile-end) 100%);
    border: 1px solid var(--tile-edge);
    color: var(--text-light); text-decoration: none;
  }
  .category-tile svg {
    position: absolute; left: 50%; top: 52px; transform: translateX(-50%);
  }
  .category-label {
    position: absolute; left: 20px; top: 128px;
    font-size: 19px; font-weight: 400; line-height: 1;
  }
  .category-tile.videos .category-label,
  .category-tile.audio .category-label { left: 16px; }

  .footer {
    position: absolute; left: 0; top: 672px; width: 1200px; height: 43px;
    background: var(--bar-bg);
    border-top: 1px solid var(--edge);
  }
  .powered-by {
    position: absolute; right: 104px; top: 12px;
    display: flex; align-items: center; gap: 7px;
    color: var(--text-muted); font-size: 12px;
  }
  .powered-square {
    width: 20px; height: 20px; border-radius: 3px; background: var(--mark-muted);
  }
</style>
</head>
<body>
<div class="app">
  <header class="top-bar">
    <div class="user-menu">
      <svg width="8" height="12" viewBox="0 0 8 12" aria-hidden="true">
        <circle cx="4" cy="3" r="2.6" fill="var(--accent)"/>
        <rect x="1" y="6" width="6" height="6" rx="1.5" fill="var(--accent)"/>
      </svg>
      <span>Welcome Username</span>
      <svg width="9" height="7" viewBox="0 0 9 7" aria-hidden="true" style="margin-left:4px">
        <path d="M0 0 H9 L4.5 7 Z" fill="var(--accent)"/>
      </svg>
    </div>
  </header>

  <main class="workspace">
    <div class="brand">
      <span class="brand-square"></span>
      <span class="brand-name">CLIPROAMER</span>
    </div>

    <nav class="categories">
      <a class="category-tile images" href="#">
        <svg width="46" height="36" viewBox="0 0 46 36" aria-hidden="true">
          <rect x="2" y="2" width="42" height="32" fill="none" stroke="#fff" stroke-width="4"/>
          <path d="M7 29 L17 17 L24 24 L30 19 L39 29 Z" fill="#fff"/>
          <circle cx="33" cy="11" r="3.5" fill="#fff"/>
        </svg>
        <span class="category-label">Images</span>
      </a>
      <a class="category-tile videos" href="#">
        <svg width="42" height="40" viewBox="0 0 42 40" aria-hidden="true">
          <path d="M2 12 L39 2 L41 9 L4 19 Z" fill="#fff"/>
          <path d="M10 9.5 L14 15 M18 7.5 L22 13 M26 5.3 L30 10.8 M34 3.2 L37 8" stroke="var(--tile-start)" stroke-width="3"/>
          <rect x="3" y="19" width="38" height="20" fill="#fff"/>
          <rect x="10" y="25" width="24" height="2.5" fill="var(--tile-start)"/>
          <rect x="10" y="31" width="24" height="2.5" fill="var(--tile-start)"/>
        </svg>
        <span class="category-label">Videos</span>
      </a>
      <a class="category-tile audio" href="#">
        <svg width="46" height="46" viewBox="0 0 46 46" aria-hidden="true">
          <circle cx="30" cy="30" r="14" fill="#fff"/>
          <circle cx="30" cy="30" r="3.5" fill="var(--tile-start)"/>
          <path d="M35 35 L40 38" stroke="var(--tile-start)" stroke-width="2"/>
          <ellipse cx="9" cy="28" rx="8" ry="6.5" fill="#fff"/>
          <path d="M15 28 L24 3 L27 4 L18 29 Z" fill="#fff"/>
          <path d="M24 3 C30 3 36 8 34 16 C33 10 29 9 26 10 Z" fill="#fff"/>
        </svg>
        <span class="category-label">Audio</span>
      </a>
    </nav>
  </main>

  <footer class="footer">
    <div class="powered-by">
      <span>Powered by Lumarra</span>
      <span class="powered-square"></span>
    </div>
  </footer>
</div>
</body>
</html>
```